Marlow Optics PowerPoint Template

Marlow Optics needs a nice new corporate PowerPoint template, to be used for all types of presentations: sales, business development, finance, board/exec, etc.

I'd like to get a clean layout that reflects the brand (www.marlowoptics.example), has a bright, interesting title slide, and then minimal graphics on the content slides. Ideally the content slides would have a header, "mo" circle part of the Marlow Optics logo (either above or below), copyright/confidential footer, and page #.

About us: we have developed a revolutionary new array camera for mobile devices, providing depth at every pixel. Focus on any subject, change focus (even on multiple subjects) after you take the photo, capture linear measurements, scale and segment your images, change backgrounds, and apply filters, all from any device.
It's not just about megapixels anymore.
See www.marlowoptics.example for info.

Target Market(s)

The audience for 90% of our presentations is highly educated executives at technology companies.

Industry/Entity Type

Camera

Requirements
Nice to have
• It would be great to show an image in a phone UI on the title slide, similar to the approach on our website.
Helpful to have tagline on title slide: "A smart camera for your smartphone." It may also fit on the content slides - feel free to try.
I attached a product photo, but using it is completely optional.
I'd like the "mo" circle on the content slides, but the whole logo on the title slides.
Thanks!

```html
<!DOCTYPE html>
<html lang="en">
<head>
<meta charset="utf-8">
<title>Marlow Optics Presentation Template</title>
<link href="https://fonts.googleapis.com/css2?family=Arimo:ital,wght@0,400;0,700;1,700&display=swap" rel="stylesheet">
<style>
  :root {
    --page-bg: #e4e4e4;
    --slide-light: #f7f7f7;
    --slide-mid: #c9c9c9;
    --brand-dark: #23505f;
    --brand-bright: #1b8aa6;
    --accent-red: #d0021b;
    --text-dark: #1d2a33;
    --device-frame: #1c1c1c;
    --screen: #ffffff;
    --grid-line: #d6d6d6;
  }
  * { box-sizing: border-box; margin: 0; padding: 0; }
  html, body { width: 1200px; height: 1200px; overflow: hidden; }
  body {
    background: var(--page-bg);
    font-family: "Arimo", Arial, sans-serif;
    color: var(--text-dark);
  }
  .deck {
    width: 1200px; height: 1200px;
    display: grid;
    grid-template-columns: 500px 500px;
    grid-template-rows: 375px 375px 375px;
    gap: 18px 40px;
    justify-content: center;
    align-content: center;
  }
  .slide {
    position: relative;
    width: 500px; height: 375px;
    overflow: hidden;
    background: radial-gradient(ellipse at center, var(--slide-light) 0%, #e6e6e6 55%, var(--slide-mid) 100%);
    box-shadow: 0 2px 8px rgba(0,0,0,0.25);
    border: 6px solid #ffffff;
  }

  /* wordmark: plain text only */
  .wordmark { color: var(--brand-dark); font-weight: 700; white-space: nowrap; }
  .wordmark-large { font-size: 34px; }
  .wordmark-small { font-size: 9px; display: flex; align-items: center; }

  /* title slide */
  .title-slide { display: flex; flex-direction: column; align-items: center; justify-content: center; gap: 22px; }
  .title-slide-heading { font-size: 44px; font-weight: 700; color: var(--brand-dark); }

  /* photo slide */
  .photo-slide .product-photo {
    position: absolute; inset: 0;
    background: linear-gradient(120deg, #f2f2f2 0%, #d4d4d4 45%, #3a3a3a 70%, #1e1e1e 100%);
  }

  /* closing slide */
  .closing-slide { display: flex; align-items: center; justify-content: center; }

  /* device frame on content slides */
  .device {
    position: absolute; left: 18px; top: 22px;
    width: 452px; height: 320px;
    background: var(--device-frame);
    border-radius: 28px;
    padding: 22px 46px 22px 20px;
  }
  .device-buttons {
    position: absolute; right: 16px; top: 70px;
    display: flex; flex-direction: column; gap: 42px;
  }
  .device-buttons span { display: block; width: 10px; height: 34px; border-radius: 3px; border: 2px solid #3d3d3d; }
  .screen { width: 100%; height: 100%; background: var(--screen); overflow: hidden; }
  .screen-header { display: flex; height: 34px; }
  .screen-header .wordmark { width: 80px; padding-left: 8px; background: var(--screen); }
  .screen-title {
    flex: 1; background: var(--brand-dark); color: #ffffff;
    font-weight: 700; font-style: italic; font-size: 17px;
    display: flex; align-items: center; padding-left: 18px;
  }
  .screen-body { padding: 16px 22px; font-size: 14.5px; line-height: 1.3; }
  .highlight { color: var(--accent-red); font-weight: 700; }
  .bullet-list { list-style: none; }
  .bullet-list li { position: relative; padding-left: 16px; margin-bottom: 2px; }
  .bullet-list li::before {
    content: ""; position: absolute; left: 0; top: 6px;
    width: 7px; height: 7px; border-radius: 50%; background: var(--brand-dark);
  }
  .chart { display: block; }
  .chart text { font-family: "Arimo", Arial, sans-serif; font-size: 8px; fill: var(--text-dark); }
</style>
</head>
<body>
<main class="deck">

  <section class="slide title-slide">
    <div class="wordmark wordmark-large">Marlow Optics</div>
    <h1 class="title-slide-heading">Title</h1>
  </section>

  <section class="slide photo-slide">
    <div class="product-photo" role="img" aria-label="Product photo of smartphones with the array camera"></div>
  </section>

  <section class="slide content-slide">
    <div class="device">
      <div class="screen">
        <header class="screen-header">
          <div class="wordmark wordmark-small">Marlow Optics</div>
          <div class="screen-title">Title</div>
        </header>
        <div class="screen-body">
          <p>Lorem ipsum dolor sit amet, consectetur adipiscing elit. Nam et dolor scelerisque, condimentum sapien id, posuere justo. <span class="highlight">Interdum et malesuada</span> fames ac ante ipsum primis in faucibus. Sed auctor mi. Quisque vel nunc.</p>
        </div>
      </div>
      <div class="device-buttons"><span></span><span></span><span></span></div>
    </div>
  </section>

  <section class="slide content-slide">
    <div class="device">
      <div class="screen">
        <header class="screen-header">
          <div class="wordmark wordmark-small">Marlow Optics</div>
          <div class="screen-title">Title</div>
        </header>
        <div class="screen-body">
          <ul class="bullet-list">
            <li>Lorem ipsum dolor sit amet, consectetur adipiscing elit.</li>
            <li>Nam et dolor scelerisque, condimentum sapien id, posuere justo.</li>
            <li><span class="highlight">Interdum et malesuada</span> fames ac ante ipsum primis in faucibus.</li>
          </ul>
        </div>
      </div>
      <div class="device-buttons"><span></span><span></span><span></span></div>
    </div>
  </section>

  <section class="slide content-slide">
    <div class="device">
      <div class="screen">
        <header class="screen-header">
          <div class="wordmark wordmark-small">Marlow Optics</div>
          <div class="screen-title">Title</div>
        </header>
        <svg class="chart" width="386" height="242" viewBox="0 0 386 242" role="img" aria-label="Bar chart of Region 1 and Region 2 from 2007 to 2010">
          <g stroke="var(--grid-line)" stroke-width="1">
            <line x1="40" y1="20" x2="40" y2="200"/>
            <line x1="85" y1="20" x2="85" y2="200"/>
            <line x1="130" y1="20" x2="130" y2="200"/>
            <line x1="175" y1="20" x2="175" y2="200"/>
            <line x1="220" y1="20" x2="220" y2="200"/>
          </g>
          <g>
            <rect x="40" y="30" width="18" height="14" fill="var(--brand-dark)"/>
            <rect x="40" y="44" width="103" height="14" fill="var(--brand-bright)"/>
            <rect x="40" y="72" width="50" height="14" fill="var(--brand-dark)"/>
            <rect x="40" y="86" width="81" height="14" fill="var(--brand-bright)"/>
            <rect x="40" y="114" width="94" height="14" fill="var(--brand-dark)"/>
            <rect x="40" y="128" width="126" height="14" fill="var(--brand-bright)"/>
            <rect x="40" y="156" width="171" height="14" fill="var(--brand-dark)"/>
            <rect x="40" y="170" width="103" height="14" fill="var(--brand-bright)"/>
          </g>
          <g text-anchor="end">
            <text x="34" y="47">2007</text>
            <text x="34" y="89">2008</text>
            <text x="34" y="131">2009</text>
            <text x="34" y="173">2010</text>
          </g>
          <g text-anchor="middle">
            <text x="40" y="214">0</text>
            <text x="85" y="214">25</text>
            <text x="130" y="214">50</text>
            <text x="175" y="214">75</text>
            <text x="220" y="214">100</text>
          </g>
          <rect x="250" y="22" width="8" height="8" fill="var(--brand-dark)"/>
          <text x="263" y="29">Region 1</text>
          <rect x="310" y="22" width="8" height="8" fill="var(--brand-bright)"/>
          <text x="323" y="29">Region 2</text>
        </svg>
      </div>
      <div class="device-buttons"><span></span><span></span><span></span></div>
    </div>
  </section>

  <section class="slide closing-slide">
    <div class="wordmark wordmark-large">Marlow Optics</div>
  </section>

</main>
</body>
</html>
```